Vemtri Gymnastics Silver gym banner

We need a banner for our new gym.
It should have navy, light blue, lilac and purple colors with our name, logo and other wording in navy color. Colors should bleed one into the other.
File with name, logo and other wording is attached.
Words: Rhythmic gymnastics, ballet, etc should be on the bottom

Target Market(s)

Girls 3 to 16 years of age

Industry/Entity Type

Athletics

Font styles to use
Other font styles liked:
• Please use fonts on file included

Colors
0054AA
0677BA
7BADD7
CADEEF
E8F1F8
0094D4
00A9DD
6FCCEA
C7EBF8
E9F6FB
00AB8E
00BBA5
67D7C9
C6EFE9
E9F9F6
6B429C
8869AF
B7A5CE
E3DAEB
F3F0F8

Requirements
Must have
• our logo and name of the gym
Nice to have
• rhythmic gymnastics feel
Should not have
• bold colors

```html
<!DOCTYPE html>
<html lang="en">
<head>
<meta charset="utf-8">
<title>Vemtri Gymnastics – School of Champions Banner</title>
<link rel="stylesheet" href="https://fonts.googleapis.com/css2?family=Poppins:wght@600;700&family=Kaushan+Script&display=swap">
<style>
  :root {
    --page-bg: #c4c4c4;
    --navy-deep: #061a45;
    --navy: #0b2a63;
    --blue-glow: #2a6cb0;
    --cyan-script: #2fd6e6;
    --white: #ffffff;
    --divider: #5a4a9a;
    --photo-pink: #c25bbf;
    --photo-rose: #d98fc4;
    --photo-skin: #e2b79c;
    --photo-aqua: #2fc3e0;
    --photo-red: #c8202a;
    --photo-blue: #1f63c4;
  }
  * { margin: 0; padding: 0; box-sizing: border-box; }
  html, body {
    width: 793px;
    height: 1200px;
    overflow: hidden;
    background: var(--page-bg);
  }
  .banner {
    position: absolute;
    left: 26px;
    top: 345px;
    width: 740px;
    height: 510px;
    overflow: hidden;
    background:
      radial-gradient(ellipse 55% 60% at 62% 18%, rgba(60,130,200,0.55), transparent 70%),
      radial-gradient(ellipse 80% 90% at 60% 40%, var(--blue-glow), var(--navy) 60%, var(--navy-deep) 100%);
    box-shadow: 0 6px 14px rgba(0,0,0,0.35);
  }
  .banner__floor {
    position: absolute;
    left: 0; right: 0; bottom: 0;
    height: 60px;
    background: linear-gradient(to bottom, transparent, rgba(4,18,50,0.45));
  }
  .brand {
    position: absolute;
    left: 44px;
    top: 55px;
    display: flex;
    align-items: center;
    gap: 14px;
  }
  .brand__dot {
    width: 34px;
    height: 34px;
    border-radius: 50%;
    background: var(--white);
  }
  .brand__name {
    font-family: 'Poppins', sans-serif;
    font-weight: 600;
    font-size: 24px;
    color: var(--white);
  }
  .headline {
    position: absolute;
    left: 42px;
    top: 122px;
  }
  .headline__script {
    display: block;
    font-family: 'Kaushan Script', cursive;
    font-size: 70px;
    line-height: 1;
    color: var(--cyan-script);
    transform: rotate(-4deg);
    transform-origin: left bottom;
    margin-left: 8px;
  }
  .headline__main {
    display: block;
    font-family: 'Poppins', sans-serif;
    font-weight: 700;
    font-size: 80px;
    line-height: 1;
    color: var(--white);
    margin-top: -8px;
    letter-spacing: -1px;
  }
  .programs {
    position: absolute;
    left: 46px;
    top: 284px;
    width: 198px;
    list-style: none;
  }
  .programs__item {
    font-family: 'Poppins', sans-serif;
    font-weight: 600;
    font-size: 16px;
    color: var(--white);
    height: 36.5px;
    line-height: 34px;
    border-bottom: 1px solid var(--divider);
  }
  .programs__item:last-child { border-bottom: none; }
  .photo {
    position: absolute;
    border-radius: 28px;
  }
  .photo--gymnasts {
    left: 548px;
    top: 0;
    width: 152px;
    height: 478px;
    border-radius: 0 0 40px 40px;
    background: linear-gradient(to bottom,
      var(--photo-red) 0%,
      var(--photo-aqua) 12%,
      var(--photo-aqua) 40%,
      var(--photo-rose) 55%,
      var(--photo-pink) 68%,
      var(--photo-skin) 84%,
      var(--photo-skin) 100%);
    opacity: 0.85;
  }
  .photo--ribbon-split {
    left: 272px;
    top: 320px;
    width: 262px;
    height: 158px;
    background: linear-gradient(to right,
      var(--photo-pink) 0%,
      var(--photo-rose) 32%,
      var(--photo-skin) 52%,
      var(--photo-blue) 72%,
      var(--photo-blue) 100%);
    opacity: 0.85;
  }
</style>
</head>
<body>
  <section class="banner">
    <div class="banner__floor"></div>
    <div class="photo photo--gymnasts" role="img" aria-label="Photo of a young gymnast on red aerial silks above a gymnast in a pink leotard holding a standing split"></div>
    <div class="photo photo--ribbon-split" role="img" aria-label="Photo of a pink rhythmic gymnastics ribbon and a young gymnast in blue sitting in a split"></div>
    <header class="brand">
      <span class="brand__dot"></span>
      <span class="brand__name">Vemtri Gymnastics</span>
    </header>
    <h1 class="headline">
      <span class="headline__script">School of</span>
      <span class="headline__main">CHAMPIONS</span>
    </h1>
    <ul class="programs">
      <li class="programs__item">Rhythmic Gymnastics</li>
      <li class="programs__item">Ballroom Dance</li>
      <li class="programs__item">Ballet</li>
      <li class="programs__item">Stretching</li>
      <li class="programs__item">Hip Hop</li>
    </ul>
  </section>
</body>
</html>
```